Brand Identity Poster - Sabor Ventana

We have a restaurant in Singapore - and looking for a graphic design on a poster - which we can use for all event signage. Our intent is to use this graphic design as a branding mechanism - that whenever the customer sees the image - they know it is Sabor Ventana.

The first photo below is one we found - that we love the combination of the feeling of the poster and the colors. Something similar to this is what we want.

The second file is our new logo.

The third and fourth files show pictures of the restaurant.

The image we wish to convey is relaxed dining - comfortable - and festive. We host a lot of events in the restaurant and we want to be the go-to place for families. We can handle up to 100 people in our restaurant - including outdoor space. Therefore many families and companies hold their gathering here.

Our food is fresh, cooked from the heart and is Filipino and Spanish Fusion. This cuisine includes a lot of seafood and pork.

We offer a great selection of tapas, wine and beer. As we are located in a Business Park, we will also use the image to announce our various "after work" specials so people can relax after hours - before going home.

In our logo - we are not entirely happy with the yellowish colors on the right side. If you have a different yellowish color that works well with the poster - then we are open to modifying the colors in the logo to better match the poster.

The last file is the AI file for the logo - in case you want to modify the colors.

We will make our decision quickly - hence this is a 5 day project.

Good luck and we look forward to your wonderful design ideas.

Project Deadline Extended Reason: Give designers time to adjust their designs based on the feedback given. Added Thursday, June 2, 2016

Hi Designers - we've been very busy in the last 2 days with the final construction of the relaunch. Posting new pictures of the decor, so you can do final design and color tweaks to match. Many thanks for all your great ideas. Added Wednesday, June 8, 2016

Target Market(s)

25 - 40 - Professionals (for professionals during lunch as this is a business park) and Families (for events on evenings and week-ends).

Industry/Entity Type

Restaurant

Requirements
Must have
• Must incorporate our logo - again open to changes in color of the logo - if that works better for you.
• Needs to match our "ventana" name.
• Works well with tapas and wine crowd.
• Have a clearly defined space on the poster - where we can announce different events, as this design will be reused on all events we host.
Nice to have
• The font should be complementary to the font in our logo name. Does not have to be identical - but looks well with the name.
Should not have
• Should not be child-like - as that is too specific of a market.

```html
<!DOCTYPE html>
<html lang="en">
<head>
<meta charset="utf-8">
<title>Sabor Ventana – Afterwork Poster Variants</title>
<link href="https://fonts.googleapis.com/css2?family=PT+Sans:wght@400;700&display=swap" rel="stylesheet">
<style>
  :root {
    --page: #ffffff;
    --brand-red: #e2312b;
    --brand-gold: #f5c843;
    --ink: #161616;

    --warm-orange: #e9892a;
    --warm-red: #e0533f;
    --leaf-green: #6ab344;
    --plum: #5b3f8f;
    --mauve: #9a5a8f;

    --a-crown: #1f4a36;
    --a-panel: #f4f6e2;
    --a-kicker: #8dbf45;
    --a-title: #57a62f;
    --a-handle: #cf5a27;
    --a-url: #4f9e2c;

    --b-crown: #1f5273;
    --b-panel: #b8d27c;
    --b-kicker: #e2312b;
    --b-title: #1f5273;
    --b-handle: #c0457e;
    --b-url: #4aa597;
    --b-yellow: #f2c12a;
  }

  * { margin: 0; padding: 0; box-sizing: border-box; }

  html, body {
    width: 1200px;
    height: 1032px;
    overflow: hidden;
    background: var(--page);
  }

  .canvas {
    position: relative;
    width: 1200px;
    height: 1032px;
    background: var(--page);
    font-family: "PT Sans", sans-serif;
  }

  .poster {
    position: absolute;
    top: 57px;
    width: 532px;
    height: 752px;
    overflow: hidden;
  }
  .poster--green { left: 48px; }
  .poster--blue  { left: 625px; }

  .poster__backdrop {
    position: absolute;
    inset: 0;
  }
  .poster--green .poster__backdrop {
    background:
      radial-gradient(circle at 15% 12%, var(--warm-red) 0 14%, transparent 30%),
      radial-gradient(circle at 88% 14%, var(--plum) 0 16%, transparent 34%),
      radial-gradient(circle at 10% 55%, var(--leaf-green) 0 12%, transparent 30%),
      radial-gradient(circle at 90% 62%, var(--mauve) 0 12%, transparent 30%),
      radial-gradient(circle at 20% 90%, var(--warm-orange) 0 14%, transparent 34%),
      radial-gradient(circle at 85% 92%, #c65a5a 0 12%, transparent 30%),
      linear-gradient(160deg, #e98a3a 0%, #9ccc6a 45%, #8c5aa0 75%, #ec7a3a 100%);
  }
  .poster--blue .poster__backdrop {
    background:
      radial-gradient(circle at 15% 12%, #e8703a 0 14%, transparent 30%),
      radial-gradient(circle at 88% 14%, #8a3f94 0 16%, transparent 34%),
      radial-gradient(circle at 10% 55%, #6fbf6a 0 12%, transparent 30%),
      radial-gradient(circle at 90% 62%, #c34a4a 0 12%, transparent 30%),
      radial-gradient(circle at 20% 90%, var(--b-yellow) 0 14%, transparent 34%),
      radial-gradient(circle at 85% 92%, #e07a3a 0 12%, transparent 30%),
      linear-gradient(160deg, #f0a02a 0%, #8cc98a 45%, #5a6fb0 75%, #f2a03a 100%);
  }

  .poster__art {
    position: absolute;
    inset: 0;
    width: 100%;
    height: 100%;
  }

  .poster__name {
    font-weight: 700;
    font-size: 38px;
    fill: var(--brand-gold);
  }
  .poster__kicker { font-size: 23px; font-weight: 400; letter-spacing: 0.5px; }
  .poster__title  { font-size: 46px; font-weight: 700; }
  .poster__dates  { font-size: 27px; font-weight: 700; fill: var(--ink); }
  .poster__handle { font-size: 16px; font-weight: 700; }
  .poster__url    { font-size: 21px; font-weight: 700; }

  .poster--green .poster__crown  { fill: var(--a-crown); }
  .poster--green .poster__panel  { fill: var(--a-panel); }
  .poster--green .poster__stem   { fill: var(--a-panel); }
  .poster--green .poster__kicker { fill: var(--a-kicker); }
  .poster--green .poster__title  { fill: var(--a-title); }
  .poster--green .poster__handle { fill: var(--a-handle); }
  .poster--green .poster__url    { fill: var(--a-url); }

  .poster--blue .poster__crown  { fill: var(--b-crown); }
  .poster--blue .poster__panel  { fill: var(--b-panel); }
  .poster--blue .poster__stem   { fill: #9fcf86; }
  .poster--blue .poster__kicker { fill: var(--b-kicker); }
  .poster--blue .poster__title  { fill: var(--b-title); }
  .poster--blue .poster__handle { fill: var(--b-handle); }
  .poster--blue .poster__url    { fill: var(--b-url); }

  .poster__base { fill: #f6f0e2; opacity: 0.75; }

  .brand-lockup {
    position: absolute;
    left: 0;
    right: 0;
    top: 922px;
    text-align: center;
    font-family: "PT Sans", sans-serif;
    font-weight: 700;
    font-size: 38px;
    letter-spacing: 1px;
    color: var(--brand-red);
  }
</style>
</head>
<body>
<main class="canvas">

  <section class="poster poster--green" aria-label="Afterwork poster, green variant">
    <div class="poster__backdrop" role="img" aria-label="Festive illustrated backdrop of overlapping fruit, chilli, leaf and swirl shapes in orange, green and purple"></div>
    <svg class="poster__art" viewBox="0 0 630 890" preserveAspectRatio="none">
      <rect class="poster__base" x="0" y="820" width="630" height="70"/>
      <rect class="poster__stem" x="313" y="600" width="27" height="230"/>
      <path class="poster__crown" d="M318 46 C400 110 520 220 553 345 Q500 310 430 320 Q380 330 350 365 Q320 395 290 370 Q260 345 200 330 Q150 320 91 345 C120 220 240 110 318 46 Z"/>
      <path class="poster__panel" d="M91 345 Q150 320 200 330 Q260 345 290 370 Q320 395 350 365 Q380 330 430 320 Q500 310 553 345 C575 450 545 560 420 610 C330 645 220 630 150 580 C90 530 78 430 91 345 Z"/>
      <text class="poster__name" x="320" y="266" text-anchor="middle" textLength="300" lengthAdjust="spacingAndGlyphs">SABOR VENTANA</text>
      <text class="poster__kicker" x="316" y="426" text-anchor="middle">SPANISH FILIPINO FUSION</text>
      <text class="poster__title" x="316" y="477" text-anchor="middle">AFTERWORK</text>
      <text class="poster__dates" x="316" y="506" text-anchor="middle">2<tspan font-size="15" dy="-11">nd</tspan><tspan dy="11"> - 8</tspan><tspan font-size="15" dy="-11">th</tspan><tspan dy="11"> JULY • 2016</tspan></text>
      <text class="poster__handle" x="326" y="578" text-anchor="middle">SABORVENTANA</text>
      <text class="poster__url" x="321" y="870" text-anchor="middle">SABORVENTANA.COM</text>
    </svg>
  </section>

  <section class="poster poster--blue" aria-label="Afterwork poster, blue variant">
    <div class="poster__backdrop" role="img" aria-label="Festive illustrated backdrop of overlapping fruit, chilli, leaf and swirl shapes in yellow, orange, teal and purple"></div>
    <svg class="poster__art" viewBox="0 0 630 890" preserveAspectRatio="none">
      <rect class="poster__base" x="0" y="820" width="630" height="70"/>
      <rect class="poster__stem" x="313" y="600" width="27" height="230"/>
      <path class="poster__crown" d="M318 46 C400 110 520 220 553 345 Q500 310 430 320 Q380 330 350 365 Q320 395 290 370 Q260 345 200 330 Q150 320 91 345 C120 220 240 110 318 46 Z"/>
      <path class="poster__panel" d="M91 345 Q150 320 200 330 Q260 345 290 370 Q320 395 350 365 Q380 330 430 320 Q500 310 553 345 C575 450 545 560 420 610 C330 645 220 630 150 580 C90 530 78 430 91 345 Z"/>
      <text class="poster__name" x="320" y="266" text-anchor="middle" textLength="300" lengthAdjust="spacingAndGlyphs">SABOR VENTANA</text>
      <text class="poster__kicker" x="316" y="426" text-anchor="middle">SPANISH FILIPINO FUSION</text>
      <text class="poster__title" x="316" y="477" text-anchor="middle">AFTERWORK</text>
      <text class="poster__dates" x="316" y="506" text-anchor="middle">2<tspan font-size="15" dy="-11">nd</tspan><tspan dy="11"> - 8</tspan><tspan font-size="15" dy="-11">th</tspan><tspan dy="11"> JULY • 2016</tspan></text>
      <text class="poster__handle" x="326" y="578" text-anchor="middle">SABORVENTANA</text>
      <text class="poster__url" x="321" y="870" text-anchor="middle">SABORVENTANA.COM</text>
    </svg>
  </section>

  <div class="brand-lockup">SABOR VENTANA</div>

</main>
</body>
</html>
```